New LLC consulting company needs a business card design

I need a business card design for new company in Alexandria Virginia called TK Verdant Consulting LLC. The company is focused on consulting for defense and national security issues with expertise in nuclear and space topics. I would like to see designs that are simple and I am open to colors except for brown.

Target Market(s)

All businesses that are seeking consulting help

Industry/Entity Type

Consulting

Contact Information for Business Card

Name of company - TK Verdant Consulting LLC; name (Delia Hawke) President; email: hawkedr41@mailbox-example.net; Phone: 555-271-9043

Requirements
Must have
• The details described above
Nice to have
• I'm open to all ideas
Should not have
• No brown

```html
<!DOCTYPE html>
<html lang="en">
<head>
<meta charset="utf-8">
<title>TK Verdant Consulting LLC — Business Card</title>
<link href="https://fonts.googleapis.com/css2?family=Lato:wght@400;700;900&display=swap" rel="stylesheet">
<style>
  :root {
    --navy: #1a3146;
    --sky: #63b3d9;
    --white: #ffffff;
    --ink: #1c2f44;
    --stage: #2e2e2e;
  }
  * { box-sizing: border-box; margin: 0; padding: 0; }
  html, body {
    width: 1200px; height: 875px; overflow: hidden;
    background: var(--stage);
    font-family: "Lato", sans-serif;
  }
  .canvas {
    width: 1200px; height: 875px;
    display: flex; align-items: center; justify-content: center; gap: 60px;
  }
  .card {
    position: relative;
    width: 525px; height: 300px;
    border-radius: 18px;
    overflow: hidden;
  }
  /* Front */
  .card-front {
    background: var(--navy);
    display: flex; align-items: center; justify-content: center; gap: 22px;
  }
  .brand-mark {
    width: 64px; height: 64px; border-radius: 50%;
    background: var(--sky); flex: none;
  }
  .brand-name {
    color: var(--white);
    font-weight: 700;
    letter-spacing: 0.06em;
    text-transform: uppercase;
    line-height: 1.15;
  }
  .card-front .brand-name { font-size: 30px; }
  .card-front .brand-name span { display: block; font-size: 30px; }

  /* Back */
  .card-back { background: var(--white); }
  .back-brand {
    position: absolute; left: 40px; top: 104px;
    display: flex; align-items: center; gap: 14px;
  }
  .back-brand .brand-mark { width: 56px; height: 56px; }
  .back-brand .brand-name {
    color: var(--ink); font-size: 17px; letter-spacing: 0.04em;
  }
  .back-brand .brand-name span { display: block; }
  .person {
    position: absolute; left: 290px; top: 82px;
    color: var(--ink);
  }
  .person-name {
    font-weight: 900; font-size: 25px; letter-spacing: 0.02em;
    text-transform: uppercase;
  }
  .person-title {
    color: var(--sky); font-size: 15px; margin-top: 2px;
  }
  .person-rule {
    width: 58px; height: 1.5px; background: var(--ink); margin: 8px 0 10px;
  }
  .contact { list-style: none; font-size: 13px; }
  .contact li { display: flex; align-items: center; gap: 8px; margin-bottom: 6px; }
  .contact .phone { font-size: 16px; }
  .contact svg { width: 12px; height: 12px; flex: none; }
  .stripe {
    position: absolute; left: 0; bottom: 0; width: 100%; height: 62px;
  }
</style>
</head>
<body>
  <main class="canvas">
    <section class="card card-front" aria-label="Card front">
      <div class="brand-mark" aria-hidden="true"></div>
      <p class="brand-name">TK Verdant<span>Consulting LLC</span></p>
    </section>

    <section class="card card-back" aria-label="Card back">
      <div class="back-brand">
        <div class="brand-mark" aria-hidden="true"></div>
        <p class="brand-name">TK Verdant<span>Consulting LLC</span></p>
      </div>

      <div class="person">
        <h1 class="person-name">Delia Hawke</h1>
        <p class="person-title">President</p>
        <div class="person-rule"></div>
        <ul class="contact">
          <li class="phone">
            <svg viewBox="0 0 24 24" aria-hidden="true"><path fill="#63b3d9" d="M6.6 10.8a15 15 0 0 0 6.6 6.6l2.2-2.2c.3-.3.7-.4 1-.2 1.1.4 2.3.6 3.6.6.6 0 1 .4 1 1V20c0 .6-.4 1-1 1A17 17 0 0 1 3 4c0-.6.4-1 1-1h3.5c.6 0 1 .4 1 1 0 1.3.2 2.5.6 3.6.1.3 0 .7-.2 1z"/></svg>
            555-271-9043
          </li>
          <li>
            <svg viewBox="0 0 24 24" aria-hidden="true"><path fill="#63b3d9" d="M2 5h20v14H2z"/><path fill="none" stroke="#fff" stroke-width="2" d="M2 5l10 8 10-8"/></svg>
            hawkedr41@mailbox-example.net
          </li>
        </ul>
      </div>

      <svg class="stripe" viewBox="0 0 525 62" preserveAspectRatio="none" aria-hidden="true">
        <polygon points="0,52 372,52 380,34 525,34 525,62 0,62" fill="#1a3146"/>
        <polygon points="384,30 525,4 525,30" fill="#63b3d9"/>
        <polygon points="388,30 525,30 525,34 386,34" fill="#63b3d9"/>
      </svg>
    </section>
  </main>
</body>
</html>
```